KLVN- company with a mission

KLVN LLC stands for keeping lanterns vividly nigh (non profit arm is called lantern kept foundation)—our business is based out of New York City and has a non-profit arm where for every bar you purchase, we donate a bar (don’t want any designs that limits us to only soap). Currently working with South Africa. We want the focus to be organic/natural soap with a mission.
What our website needs to…achieve:
Purpose = branding, building up interesting leaving up to launch date, then a full functional site for selling soap (for now) with a mission. With that said, there will need to be a page designed for “COMING SOON” – with a place to post our teaser 30 second video (kind of like a commercial/movie trailer) – until everything else is done.
We are the first in the industry to do one for one (or …50/50). Most companies that do charity work are mostly for every $$$ we donate $0.10, or 1% of XXX. We are starting out to run the non-profit arm as well not just after we reach certain milestones. In addition, we will be transparent for the non-profit side whereas most of the time when you donate, you have no idea where the money ends up going.
IN ADDITION: we still need to be clean/elegant – and selling our soap; so website will need to 1. Showcase our products, 2. Be very clear that we have a mission (not sure if there is a way to show case both our soap AND our mission)
Some sites we like:
Pelarin.com—like them in terms of business model—in terms of their website: like how their site is clean and friendly, but it seems too cluttered
www.quendaltrove.com -- similar business model, www.fevriskel.com, brimavault.com, marshlintsoap.com
Tivel.com: like this a lot better than gavroue.com, however, major dislike of the typeface. Okay about the neutral colors…although feel like we need something a bit more cheerful here and there for our mission
Zkindle.net, brimavault.com, fennawick.com: like how they are clean and showcase well
**** However, our site also needs to convey messages like: www.wellspringpledge.org, www.rinsewidely.org
Looking for a clean, simple design. Modern, clutter-free, and inviting. Definitely do not want an arts and crafty/flowery feel. We do need something…cheerful for our nonprofit purposes.
Examples of sites we don’t like: quillmarbet.com, corvelpatchsoap.com
7 pages/ tabs maybe? (About us…video page (to show case what we are doing –currently my partner is in South Africa filming what our mission will be able to do – give children and those in need soap), FAQs, soap products, terms & conditions, contact us page, blog page……nothing too crazy).
For now, for designing purposes, please use any example texts whether it’s the about us page, mission page..policies.. and for the soap/products pages—please use example you can find online – it is fine, we just need the design done for now.
I have also attached our logo file. Please let me know if you have any questions! Thanks!
Something to consider....
pelarin.com and quendaltrove.com are probably our largest competitor out of all the websites I mentioned as they have a very similar business model where it is is a company with a mission. Homepage makes that clear that for every pair of shoes/ glasses you purchase, they give a pair. Another thing to note...is that they have been in business for a few years so their website probably have changed to more commercial than focusing/marketing on the mission of doing good. While we don't want that to be the total focus, we do need it to be present on the homepage/front page.

```html
<!DOCTYPE html>
<html lang="en">
<head>
<meta charset="utf-8">
<title>KLVN — Soap Products</title>
<link rel="stylesheet" href="https://fonts.googleapis.com/css2?family=Josefin+Sans:wght@300;400;600&family=Varela+Round&display=swap">
<style>
:root{
  --page:#f1f1f1;
  --ink:#3d3d3d;
  --muted:#6f6f6f;
  --dark:#2c2c2c;
  --slate:#555555;
  --orange:#ec9a52;
  --orange-soft:#f2a566;
  --price:#f0883e;
  --blue:#1b9ad6;
  --rule:#bdbdbd;
  --white:#ffffff;
}
*{box-sizing:border-box;margin:0;padding:0}
html,body{width:752px;height:1200px;overflow:hidden}
body{background:var(--page);font-family:"Josefin Sans",sans-serif;color:var(--ink);position:relative}
.abs{position:absolute}

.topbar{left:0;top:0;width:752px;height:36px;background:var(--dark)}
.account-links{left:80px;top:0;height:36px;display:flex;align-items:center;gap:8px;color:#dcdcdc;font-size:10px}
.account-icon{width:22px;height:22px;border:2px solid #fff;border-radius:50%}
.cart{left:538px;top:0;width:130px;height:36px;background:var(--blue);color:#fff;font-size:10px;display:flex;align-items:center;justify-content:center;gap:5px}

.social{left:80px;top:72px;display:flex;gap:3px}
.social span{width:24px;height:24px;border-radius:50%;background:#8a8a8a;display:block}

.nav-rule{left:0;top:126px;width:752px;height:2px;background:#a9a9a9}
.nav{top:140px;font-size:10px;color:#444;letter-spacing:.2px}
.brand-mark{left:318px;top:74px;width:116px;height:116px;border-radius:50%;background:var(--orange-soft);border:3px solid #fff;display:flex;align-items:center;justify-content:center;color:#fff;font-size:30px;font-weight:600;letter-spacing:1px}

.hero{left:0;top:162px;width:752px;height:140px;background:linear-gradient(90deg,#6b5a48 0%,#8a7763 40%,#7a6a58 100%)}
.hero-photo{left:430px;top:162px;width:170px;height:140px;background:linear-gradient(180deg,#8b7a66,#b79d86)}
.hero-title{left:84px;top:228px;color:#fff;font-size:22px;font-weight:400;letter-spacing:-.3px}
.hero-sub{left:85px;top:252px;color:#fff;font-size:10px}

.crumb{left:82px;top:324px;font-size:6px;color:var(--muted)}
.page-title{left:82px;top:334px;font-size:21px;font-weight:300;color:#555;letter-spacing:-.5px}
.sort{left:450px;top:331px;width:217px;height:24px;background:#fff;border:1px solid #ccc;font-size:8px;color:#666;padding:8px 10px}
.sort svg{position:absolute;right:8px;top:10px}
.title-rule{left:79px;top:361px;width:588px;height:1px;background:var(--rule)}

.sidebar{left:80px;top:391px;width:146px;height:193px;background:#fff}
.filter{position:absolute;left:7px;width:132px;border:1px solid #ddd;background:#fff;font-size:7.5px;color:#555;letter-spacing:.3px}
.filter-row{height:29px;padding:10px 9px;border-bottom:1px solid #ddd;position:relative}
.filter-row:last-child{border-bottom:0}
.filter-row .plus{position:absolute;right:9px;top:8px;font-size:10px;color:#999}

.product{width:124px;position:absolute}
.product-shot{height:76px;border-radius:3px}
.shelf{height:8px;margin-top:2px;background:linear-gradient(180deg,#e6e6e6,#f1f1f1);border-radius:3px}
.product-name{font-family:"Varela Round",sans-serif;font-size:10px;color:#4b4b4b;margin-top:12px}
.product-price{font-family:"Varela Round",sans-serif;font-size:9.5px;color:var(--price);margin-top:4px}

.grid-rule{left:82px;top:838px;width:588px;height:1px;background:#9a9a9a}

.panel{width:288px;height:99px;background:#fff;top:858px}
.panel-inner{position:absolute;left:11px;top:8px;width:267px;height:83px;color:#fff;text-align:center}
.mission{background:var(--orange)}
.mission h2{font-weight:400;font-size:24px;margin-top:19px}
.mission p{font-size:8.5px;line-height:14px;margin-top:4px}
.shipping{background:var(--slate)}
.shipping p{font-size:11px;line-height:13px;margin-top:6px}

.footer{left:79px;top:1015px;width:590px;height:148px;background:#fff;border-top:2px solid #444;border-bottom:2px solid #666}
.footer-mark{left:343px;top:988px;width:62px;height:62px;border-radius:50%;background:#444;border:3px solid #fff;box-shadow:0 0 0 1px #444;color:#fff;font-size:14px;font-weight:600;display:flex;align-items:center;justify-content:center}
.foot-col{position:absolute;top:44px;font-size:7px;color:#666}
.foot-col h3{font-size:9.5px;font-weight:400;color:#555;margin-bottom:14px}
.foot-col li{list-style:none;height:15.5px}
.email{left:498px;top:1124px;width:96px;height:18px;border:1px solid #bbb;background:#fff;font-size:6px;color:#777;padding:6px 5px}
.submit{left:600px;top:1123px;width:44px;height:20px;background:var(--orange);color:#fff;font-size:8.5px;text-align:center;padding-top:6px}
.legal{top:1179px;font-size:7px;color:#777}
</style>
</head>
<body>

<div class="abs topbar"></div>
<div class="abs account-links"><span class="account-icon"></span><span>My Account &nbsp;/&nbsp; Checkout &nbsp;/&nbsp; Search</span></div>
<div class="abs cart">
  <svg width="14" height="12" viewBox="0 0 14 12" fill="none" stroke="#fff" stroke-width="1.2"><path d="M0 1h2.5l2 7h7l1.5-5H4"/><circle cx="5.5" cy="10.5" r="1"/><circle cx="10.5" cy="10.5" r="1"/></svg>
  <span>Cart - 0 Item - &nbsp;$-0.00</span>
</div>

<div class="abs social" aria-label="Social links"><span></span><span></span><span></span><span></span></div>

<div class="abs nav-rule"></div>
<div class="abs nav" style="left:82px">HOME</div>
<div class="abs nav" style="left:152px">VIDEOS</div>
<div class="abs nav" style="left:226px">SOAP PRODUCTS</div>
<div class="abs nav" style="left:459px">BLOG PAGE</div>
<div class="abs nav" style="left:546px">FAQS</div>
<div class="abs nav" style="left:606px">CONTACT US</div>

<div class="abs hero" role="img" aria-label="Weathered wooden backdrop with a palm frond"></div>
<div class="abs hero-photo" role="img" aria-label="Two children holding a handwritten hope sign"></div>
<div class="abs hero-title">FOR EVERY PAIR PURCHASED</div>
<div class="abs hero-sub">A PAIR IS DISTRIBUTED TO SOMEONE IN NEED</div>

<div class="abs brand-mark">KLVN</div>

<div class="abs crumb">Home &gt; Soap Products &gt; Page 1 of 1</div>
<h1 class="abs page-title">OUR PRODUCTS</h1>
<div class="abs sort">SORT BY<svg width="7" height="4" viewBox="0 0 7 4"><path d="M0 0h7L3.5 4z" fill="#555"/></svg></div>
<div class="abs title-rule"></div>

<aside class="abs sidebar">
  <div class="filter" style="top:9px"><div class="filter-row">FEATURED SHOPS<span class="plus">+</span></div></div>
  <div class="filter" style="top:44px;border-top:2px solid #ddd">
    <div class="filter-row">Filter By</div>
    <div class="filter-row">GRIND<span class="plus">+</span></div>
    <div class="filter-row">ROAST<span class="plus">+</span></div>
    <div class="filter-row">COUNTRY<span class="plus">+</span></div>
    <div class="filter-row">PRICE<span class="plus">+</span></div>
  </div>
</aside>

<div class="product" style="left:253px;top:388px"><div class="product-shot" role="img" aria-label="Stack of boxed herbal soaps" style="background:linear-gradient(135deg,#7a4a2a,#c9c56a 60%,#9cc48a)"></div><div class="shelf"></div><div class="product-name">Buy One Donate One</div><div class="product-price">US $7.16</div></div>
<div class="product" style="left:397px;top:388px"><div class="product-shot" role="img" aria-label="Round beige soap bar" style="background:radial-gradient(ellipse at center,#d7c8b8 45%,transparent 70%)"></div><div class="shelf"></div><div class="product-name">Buy One Donate One</div><div class="product-price">US $7.16</div></div>
<div class="product" style="left:539px;top:388px"><div class="product-shot" role="img" aria-label="Wrapped orange soap bar" style="background:radial-gradient(ellipse at center,#f08a2a 45%,transparent 70%)"></div><div class="shelf"></div><div class="product-name">Buy One Donate One</div><div class="product-price">US $7.16</div></div>

<div class="product" style="left:253px;top:528px"><div class="product-shot" role="img" aria-label="Clear blue glycerin soap block" style="background:radial-gradient(ellipse at center,#2fb4ea 45%,transparent 70%)"></div><div class="shelf"></div><div class="product-name">Buy One Donate One</div><div class="product-price">US $7.16</div></div>
<div class="product" style="left:397px;top:528px"><div class="product-shot" role="img" aria-label="Pale blue oval soap bar with lather" style="background:radial-gradient(ellipse at center,#7fd0dc 40%,transparent 70%)"></div><div class="shelf"></div><div class="product-name">Buy One Donate One</div><div class="product-price">US $7.16</div></div>
<div class="product" style="left:539px;top:528px"><div class="product-shot" role="img" aria-label="Lilac soap bar" style="background:radial-gradient(ellipse at center,#c89ac8 42%,transparent 70%)"></div><div class="shelf"></div><div class="product-name">Buy One Donate One</div><div class="product-price">US $7.16</div></div>

<div class="product" style="left:253px;top:682px"><div class="product-shot" role="img" aria-label="Boxed goat milk soap with cream bar" style="background:radial-gradient(ellipse at center,#e8e4b8 40%,transparent 70%)"></div><div class="shelf"></div><div class="product-name">Buy One Donate One</div><div class="product-price">US $7.16</div></div>
<div class="product" style="left:397px;top:682px"><div class="product-shot" role="img" aria-label="White oval beauty bar" style="background:radial-gradient(ellipse at center,#ffffff 40%,transparent 70%)"></div><div class="shelf"></div><div class="product-name">Buy One Donate One</div><div class="product-price">US $7.16</div></div>
<div class="product" style="left:539px;top:682px"><div class="product-shot" role="img" aria-label="Brown boxed shea butter soap" style="background:radial-gradient(ellipse at center,#6a3a1e 40%,transparent 70%)"></div><div class="shelf"></div><div class="product-name">Buy One Donate One</div><div class="product-price">US $7.16</div></div>

<div class="abs grid-rule"></div>

<section class="abs panel" style="left:78px">
  <div class="panel-inner mission"><h2>OUR MISSION</h2><p>DO GOOD &nbsp;For every pair purchased<br>a pair is distributed to someone in need</p></div>
</section>
<section class="abs panel" style="left:388px">
  <div class="panel-inner shipping">
    <svg width="46" height="24" viewBox="0 0 46 24" style="margin-top:18px" fill="#fff"><rect x="10" y="2" width="22" height="14"/><path d="M33 6h6l5 6v4H33z"/><rect x="2" y="5" width="6" height="1.5"/><rect x="0" y="9" width="8" height="1.5"/><circle cx="16" cy="19" r="3.5"/><circle cx="38" cy="19" r="3.5"/></svg>
    <p>FREE SHIPPING on all orders of<br>$25 or more</p>
  </div>
</section>

<footer class="abs footer">
  <div class="foot-col" style="left:19px"><h3>ABOUT PELARIN</h3><ul><li>Rowan Ettrick's Bio</li><li>Company Information</li><li>Corporate Responsibility</li><li>Affiliate Program</li></ul></div>
  <div class="foot-col" style="left:163px"><h3>GET HELP</h3><ul><li>Track My Order</li><li>Returns</li><li>Contact Information</li><li>Questions</li></ul></div>
  <div class="foot-col" style="left:301px"><h3>EXPLORE</h3><ul><li>OUR HISTORY</li><li>DO GOOD</li><li>DESIGN</li><li>BLOG</li></ul></div>
  <div class="foot-col" style="left:417px"><h3>CONTACT US</h3><ul><li>Find a Store</li><li>SIGN UP FOR EMAILS</li></ul></div>
  <div class="foot-col" style="left:493px;top:72px;border-left:1px solid #ccc;padding-left:5px;height:30px;line-height:10px">Also Get Latest News<br>or Information</div>
</footer>
<div class="abs footer-mark">KLVN</div>
<div class="abs email">Email...</div>
<div class="abs submit">Submit</div>

<div class="abs legal" style="left:86px">Our Privacy Policy and Terms of Use</div>
<div class="abs legal" style="left:557px">Copyright 2014 Klvnlantern.com</div>

</body>
</html>
```